Project Brightvale Wellness

We need a business/ logo card design for our company based out of Canada. We will be retailing cannibus products to our customers.
For colors I've found this online : https://www.huetrackr.example/palette-results/?colors=70ff02,ff0270,ff4a02,02e1ff . We especially like the green and blue .
We would like our business card design to communicate modern medicine .

Target Market(s)

males 20-40 years

Industry/Entity Type

Health And Wellness

Contact Information for Business Card

Address is : 248 Dunmore Ave E
Toronto, ON K7R 3T8
website: www.brightvalewellness.example

Font styles to use
Serif

Requirements
Must have
• clear, easy to read logo
Nice to have
• contrasting colors
Should not have
• we want to stay away from marijuana leaf

```html
<!DOCTYPE html>
<html lang="en">
<head>
<meta charset="utf-8">
<title>Brightvale Wellness – Business Card</title>
<link rel="stylesheet" href="https://fonts.googleapis.com/css2?family=Lato:wght@400;700&family=Raleway:wght@600&display=swap">
<style>
  :root {
    --backdrop: #3a3a3a;
    --card: #050505;
    --green: #7ed321;
    --blue: #1aa9f0;
    --text: #e6e6e6;
    --rule: #555555;
  }
  * { margin: 0; padding: 0; box-sizing: border-box; }
  html, body { width: 1200px; height: 900px; overflow: hidden; }
  body {
    background: var(--backdrop);
    display: flex;
    align-items: center;
    justify-content: center;
    gap: 60px;
    font-family: "Lato", Arial, sans-serif;
  }
  .card {
    width: 520px;
    height: 300px;
    background: var(--card);
    border-radius: 22px;
    position: relative;
  }
  /* Front */
  .card-front { display: flex; align-items: center; padding: 0 36px; }
  .brand-block {
    width: 210px;
    display: flex;
    flex-direction: column;
    align-items: center;
    gap: 16px;
  }
  .brand-mark {
    width: 70px; height: 70px;
    border-radius: 50%;
    border: 5px solid var(--green);
  }
  .brand-name {
    font-family: "Raleway", Arial, sans-serif;
    font-weight: 600;
    color: var(--green);
    font-size: 26px;
    line-height: 1.1;
    text-align: center;
  }
  .divider {
    width: 1px; height: 150px;
    background: var(--rule);
    margin: 0 22px 0 10px;
  }
  .contact { color: var(--text); font-size: 14px; line-height: 1.35; }
  .person-name { font-weight: 700; font-size: 17px; letter-spacing: .5px; }
  .person-name .first { color: var(--green); }
  .person-name .last { color: var(--blue); }
  .address { margin-bottom: 8px; }
  .contact-line { display: flex; align-items: center; gap: 7px; }
  .contact-icon {
    width: 13px; height: 13px;
    background: var(--blue);
    border-radius: 2px;
    flex: none;
  }
  /* Back */
  .card-back {
    display: flex;
    flex-direction: column;
    align-items: center;
    justify-content: center;
    gap: 26px;
  }
  .card-back .brand-mark { width: 120px; height: 120px; border-width: 7px; }
  .card-back .brand-name { font-size: 42px; }
</style>
</head>
<body>
  <section class="card card-front" aria-label="Business card front">
    <div class="brand-block">
      <div class="brand-mark"></div>
      <div class="brand-name">Brightvale Wellness</div>
    </div>
    <div class="divider"></div>
    <div class="contact">
      <div class="person-name"><span class="first">DANA</span> <span class="last">WHITLOCK</span></div>
      <div class="job-title">Managing Director</div>
      <div class="address">248 Dunmore Ave E<br>Toronto, ON K7R 3T8</div>
      <div class="contact-line">
        <svg class="contact-icon" viewBox="0 0 13 13"><rect width="13" height="13" rx="2" fill="#1aa9f0"/><rect x="4" y="2.5" width="5" height="8" rx="1" fill="none" stroke="#fff" stroke-width="1.2"/></svg>
        <span>555 210 0000</span>
      </div>
      <div class="contact-line">
        <svg class="contact-icon" viewBox="0 0 13 13"><rect width="13" height="13" rx="2" fill="#1aa9f0"/><rect x="2.5" y="3.5" width="8" height="6" fill="none" stroke="#fff" stroke-width="1.1"/><path d="M2.5 3.5 6.5 7 10.5 3.5" fill="none" stroke="#fff" stroke-width="1.1"/></svg>
        <span>info@brightvale.example</span>
      </div>
      <div class="contact-line">
        <svg class="contact-icon" viewBox="0 0 13 13"><rect width="13" height="13" rx="2" fill="#1aa9f0"/><circle cx="6.5" cy="6.5" r="3.8" fill="none" stroke="#fff" stroke-width="1.1"/><path d="M2.7 6.5h7.6M6.5 2.7c-2 2.4-2 5.2 0 7.6M6.5 2.7c2 2.4 2 5.2 0 7.6" fill="none" stroke="#fff" stroke-width=".8"/></svg>
        <span>www.brightvalewellness.example</span>
      </div>
    </div>
  </section>

  <section class="card card-back" aria-label="Business card back">
    <div class="brand-mark"></div>
    <div class="brand-name">Brightvale Wellness</div>
  </section>
</body>
</html>
```